Business Card Design

We need a business card design for a new company based in Allen, Texas. (outside of Dallas,Texas) We offer Business Management Solutions to Entrepreneurs, as well as Corporate Businesses. Our product line offers solutions to Image, Branding, Social Media marketing, business development strategies, banking / funding solutions, just to name a few. We would like to see designs that convey strength and confidence. I have attached a sample design of our company name. Designers you may use company name as either: Tovan or Tovan Corporation, depending on the design layout.

Please show alternate color of Black as well.

Industry/Entity Type

Business

Contact Information for Business Card

Tovan Corporation

4862 N. Brisbury Lane, STE 300
Harlow, TX 75289
Office: 512.638.4471
Fax: 512.638.4472

Dr. Louis Brennick
Business Development Director

```html
<!DOCTYPE html>
<html lang="en">
<head>
<meta charset="utf-8">
<title>Tovan Corporation — Business Card</title>
<link rel="stylesheet" href="https://fonts.googleapis.com/css2?family=Cinzel:wght@400;600&display=swap">
<style>
  :root {
    --page-bg: #ffffff;
    --card-edge: #3b3c4a;
    --blue-light: #5b86c9;
    --blue-deep: #2c3674;
    --night-edge: #15161c;
    --night-mid: #30313a;
    --ink-dark: #1c1d33;
    --seal-light: #7a5a9c;
    --seal-deep: #2a1a3c;
    --seal-ring: #2b2b36;
    --seal-text: #ece4f2;
    --bullet: #d4456e;
  }
  html, body {
    margin: 0;
    width: 1200px;
    height: 900px;
    overflow: hidden;
    background: var(--page-bg);
  }
  .canvas { display: block; width: 1200px; height: 900px; }
  .card-edge { fill: none; stroke: var(--card-edge); stroke-width: 2; }
  .company-name {
    font-family: "Cinzel", serif;
    font-size: 27px;
    fill: var(--ink-dark);
    letter-spacing: 0.5px;
  }
  .seal-name {
    font-family: "Cinzel", serif;
    font-weight: 600;
    font-size: 13px;
    fill: var(--seal-text);
    letter-spacing: 1px;
  }
  .contact-line {
    font-family: "Cinzel", serif;
    font-size: 8.6px;
    fill: var(--ink-dark);
  }
  .contact-bullet { fill: var(--bullet); }
</style>
</head>
<body>
<svg class="canvas" viewBox="0 0 640 480" xmlns="http://www.w3.org/2000/svg">
  <defs>
    <path id="card-shape" d="M4,0 H318 A20,20 0 0 1 338,20 V194 A4,4 0 0 1 334,198 H20 A20,20 0 0 1 0,178 V4 A4,4 0 0 1 4,0 Z"/>
    <clipPath id="card-clip"><use href="#card-shape"/></clipPath>
    <radialGradient id="blue-glow" cx="170" cy="95" r="190" gradientUnits="userSpaceOnUse">
      <stop offset="0" stop-color="var(--blue-light)"/>
      <stop offset="0.6" stop-color="var(--blue-deep)"/>
      <stop offset="1" stop-color="var(--blue-deep)"/>
    </radialGradient>
    <linearGradient id="night-band" x1="0" x2="1" y1="0" y2="0">
      <stop offset="0" stop-color="var(--night-edge)"/>
      <stop offset="0.5" stop-color="var(--night-mid)"/>
      <stop offset="1" stop-color="var(--night-edge)"/>
    </linearGradient>
    <radialGradient id="seal-fill" cx="0.5" cy="0.45" r="0.55">
      <stop offset="0" stop-color="var(--seal-light)"/>
      <stop offset="1" stop-color="var(--seal-deep)"/>
    </radialGradient>
    <g id="card-body">
      <g clip-path="url(#card-clip)">
        <rect width="338" height="198" fill="url(#blue-glow)"/>
        <path d="M0,95 C60,85 115,108 170,124 C230,140 290,100 338,80 V198 H0 Z" fill="url(#night-band)"/>
      </g>
      <use href="#card-shape" class="card-edge"/>
      <circle cx="170" cy="123" r="37" fill="var(--seal-ring)"/>
      <circle cx="170" cy="123" r="32" fill="url(#seal-fill)"/>
      <text class="seal-name" x="170" y="127.5" text-anchor="middle">TOVAN</text>
    </g>
  </defs>

  <g class="card card-front" transform="translate(125 25)">
    <use href="#card-body"/>
    <text class="company-name" x="169" y="52" text-anchor="middle">TOVAN CORPORATION</text>
  </g>

  <g class="card card-back" transform="translate(128 238)">
    <g transform="scale(1.027 1.03)"><use href="#card-body"/></g>
    <g class="contact-list">
      <circle class="contact-bullet" cx="18.5" cy="19" r="3.3"/>
      <text class="contact-line" x="25" y="21">4862 N. BRISBURY LANE</text>
      <text class="contact-line" x="25" y="31">STE 300 HARLOW, TX 75289</text>
      <circle class="contact-bullet" cx="18.5" cy="53" r="3.3"/>
      <text class="contact-line" x="25" y="56">OFFICE: 512.638.4471</text>
      <circle class="contact-bullet" cx="18.5" cy="77" r="3.3"/>
      <text class="contact-line" x="25" y="80">FAX: 512.638.4472</text>
    </g>
  </g>
</svg>
</body>
</html>
```